BRAYSTONE WORKWRIGHTS, INC. ELECTRICAL SERVICE

We need a tri-fold pamphlet design for electrical service based in NW Arkansas. We offer Commercial and Industrial Electrical Services including: Infrared imaging, Data Cable Testing, Fiber Optics Testing & Repair, Utility Locates, Preventative Maintenance, Lighting Inspections, Electrical Equipment Cleaning, Automatic Transfer Switch Testing, LED Upgrades with Energy Savings Report.

```html
<!DOCTYPE html>
<html lang="en">
<head>
<meta charset="utf-8">
<title>Braystone Workwrights – Tri-fold Pamphlet</title>
<link rel="stylesheet" href="https://fonts.googleapis.com/css2?family=Open+Sans:wght@400;600;700&display=swap">
<style>
  :root {
    --backdrop: #a4a4a4;
    --brand-blue: #2143a3;
    --brand-blue-deep: #17358e;
    --tick-blue: #2e5cd6;
    --ink: #1d1d1d;
    --night: #050505;
    --paper: #ffffff;
    --mist: #ececec;
    --text-font: "Open Sans", Arial, sans-serif;
  }
  * { box-sizing: border-box; margin: 0; padding: 0; }
  html, body { width: 1200px; height: 800px; overflow: hidden; }
  body { background: var(--backdrop); font-family: var(--text-font); position: relative; }

  .brochure {
    position: absolute; left: 45px; top: 30px;
    width: 1110px; height: 740px;
    background: var(--paper);
    box-shadow: 0 18px 40px rgba(0,0,0,.28);
    overflow: hidden;
  }
  .brochure-art { position: absolute; inset: 0; }

  /* Panel 1 — About */
  .about-tab {
    position: absolute; left: 0; top: 70px;
    width: 250px; height: 56px;
    background: var(--brand-blue);
    border-radius: 0 28px 28px 0;
    color: var(--paper); font-weight: 700; font-size: 30px;
    padding: 6px 0 0 52px;
  }
  .about-copy {
    position: absolute; left: 52px; top: 150px; width: 290px;
    color: var(--ink); font-size: 15.5px; line-height: 1.55;
    text-align: justify;
  }

  /* Panel 2 — testimonial & contact */
  .testimonial {
    position: absolute; left: 400px; top: 36px; width: 315px;
    color: var(--paper); font-size: 14px; line-height: 1.42;
  }
  .testimonial .quote-mark { color: var(--brand-blue); font-size: 42px; font-weight: 700; line-height: .6; display: block; height: 20px; }
  .testimonial .highlight { color: var(--brand-blue); font-weight: 600; }
  .testimonial .attribution { display: block; margin-top: 4px; font-weight: 600; }

  .contact-list {
    position: absolute; left: 400px; top: 545px; width: 320px;
    list-style: none; color: var(--paper); font-size: 14px; line-height: 1.35;
  }
  .contact-list li { display: flex; align-items: center; gap: 16px; margin-bottom: 12px; }
  .contact-list svg { width: 22px; height: 22px; flex: none; }

  /* Panel 3 — cover */
  .cover-name {
    position: absolute; left: 790px; top: 62px;
    display: flex; align-items: center; gap: 10px;
  }
  .cover-name .mark-dot { width: 18px; height: 18px; border-radius: 50%; background: var(--brand-blue); }
  .cover-name .company { color: var(--ink); font-weight: 700; font-size: 17px; letter-spacing: .3px; }
  .tagline { position: absolute; left: 818px; top: 90px; color: var(--brand-blue); font-size: 12px; font-weight: 600; }

  .service-list {
    position: absolute; left: 790px; top: 556px; width: 312px;
    list-style: none; color: var(--paper); font-size: 13px; line-height: 1.25;
  }
  .service-list li { display: flex; align-items: flex-start; gap: 10px; margin-bottom: 5px; }
  .service-list svg { width: 18px; height: 14px; flex: none; margin-top: 2px; }
</style>
</head>
<body>
<main class="brochure">
  <svg class="brochure-art" width="1110" height="740" viewBox="0 0 1110 740">
    <rect class="panel-middle-ground" x="370" y="0" width="370" height="740" fill="var(--night)"/>
    <rect class="panel-cover-ground" x="740" y="0" width="370" height="740" fill="var(--mist)"/>
    <path class="blue-sweep" d="M0,650 C140,600 280,520 370,430 C460,345 600,330 740,360 L800,440 L800,740 L0,740 Z" fill="var(--brand-blue)"/>
    <path class="cover-sweep" d="M740,440 C860,470 1000,420 1110,300 L1110,740 L740,740 Z" fill="var(--night)"/>
    <path class="cover-blue-edge" d="M740,360 L800,440 L800,740 L740,740 Z" fill="var(--brand-blue-deep)"/>
    <line x1="370" y1="0" x2="370" y2="740" stroke="rgba(0,0,0,.12)"/>
    <line x1="740" y1="0" x2="740" y2="740" stroke="rgba(0,0,0,.12)"/>

    <polygon points="335,540 262,664 118,664 45,540 118,416 262,416" fill="var(--brand-blue)"/>
    <polygon role="img" aria-label="Photo: hands working over electrical plans with a ruler" points="322,540 256,652 124,652 58,540 124,428 256,428" fill="#d9dcdf"/>

    <g class="service-photos" transform="translate(0,75)">
      <polygon role="img" aria-label="Photo: stacked steel bearings" points="650,250 620,302 560,302 530,250 560,198 620,198" fill="#6b6f74"/>
      <polygon points="568,360 534,419 466,419 432,360 466,301 534,301" fill="var(--paper)"/>
      <polygon role="img" aria-label="Photo: technician working at an electrical panel" points="560,360 530,412 470,412 440,360 470,308 530,308" fill="#8a8f96"/>
      <polygon points="688,362 654,421 586,421 552,362 586,303 654,303" fill="var(--paper)"/>
      <polygon role="img" aria-label="Photo: blue fiber optic cables" points="680,362 650,414 590,414 560,362 590,310 650,310" fill="#2f5fb8"/>
      <polygon points="778,290 744,349 676,349 642,290 676,231 744,231" fill="var(--paper)"/>
      <polygon role="img" aria-label="Photo: field worker locating underground utilities" points="770,290 740,342 680,342 650,290 680,238 740,238" fill="#8a9a5b"/>
      <polygon points="872,238 838,297 770,297 736,238 770,179 838,179" fill="var(--brand-blue)"/>
      <polygon role="img" aria-label="Photo: hand holding a data cable tester" points="864,238 834,290 774,290 744,238 774,186 834,186" fill="#4a79c9"/>
      <polygon points="906,352 872,411 804,411 770,352 804,293 872,293" fill="var(--brand-blue)"/>
      <polygon role="img" aria-label="Photo: handheld thermal imaging camera" points="898,352 868,404 808,404 778,352 808,300 868,300" fill="#d9a21a"/>
      <polygon points="808,412 774,471 706,471 672,412 706,353 774,353" fill="var(--paper)"/>
      <polygon role="img" aria-label="Photo: gears labelled preventive maintenance" points="800,412 770,464 710,464 680,412 710,360 770,360" fill="#9a8a6e"/>
      <polygon role="img" aria-label="Photo: technician inspecting a light fixture" points="960,412 930,464 870,464 840,412 870,360 930,360" fill="#d5d9de"/>
    </g>
  </svg>

  <h2 class="about-tab">About Us</h2>
  <p class="about-copy">Since 1972, Braystone has been serving Northwest Arkansas. As our customers needed more services, we expanded our workforce, our equipment, our technology, and our capacity to meet those needs. Today, we provide complete contracting and engineering services for clients across the nation and around the world.</p>

  <blockquote class="testimonial">
    <span class="quote-mark">&ldquo;</span>
    We know that the very minor problems that did come up, your teams were always on the spot getting the issues resolved. We also know that both your teams have worked tirelessly to keep our plant going. Not only did they complete excellent quality work and they did this all with a fantastic attitude and willing disposition.
    <span class="highlight">We really appreciate all that you do.</span>
    <span class="attribution">Dale Hensley, Larkin Foods</span>
  </blockquote>

  <ul class="contact-list">
    <li>
      <svg viewBox="0 0 24 24" fill="none" stroke="#fff" stroke-width="1.8"><path d="M12 22s7-7 7-12a7 7 0 0 0-14 0c0 5 7 12 7 12z"/><circle cx="12" cy="10" r="2.5"/></svg>
      <span>1850 Kessler Road<br>Post Office Box 4420, Elm Springs, AR 72728</span>
    </li>
    <li>
      <svg viewBox="0 0 24 24" fill="#fff"><path d="M3 9c0-3 18-3 18 0v2h-4V9H7v2H3z"/><path d="M6 12h12l2 8H4z"/></svg>
      <span>479-555-0140</span>
    </li>
    <li>
      <svg viewBox="0 0 24 24" fill="#fff"><rect x="7" y="3" width="10" height="6"/><rect x="3" y="9" width="18" height="9" rx="2"/><rect x="7" y="15" width="10" height="6" fill="#2143a3" stroke="#fff" stroke-width="1.5"/></svg>
      <span>479-555-0199</span>
    </li>
    <li>
      <svg viewBox="0 0 24 24" fill="none" stroke="#fff" stroke-width="1.8"><rect x="3" y="6" width="18" height="12"/><path d="M3 6l9 7 9-7"/></svg>
      <span>support@braystone-works.net</span>
    </li>
    <li>
      <svg viewBox="0 0 24 24" fill="none" stroke="#fff" stroke-width="1.5"><circle cx="12" cy="12" r="9"/><ellipse cx="12" cy="12" rx="4" ry="9"/><path d="M3 12h18M5 7h14M5 17h14"/></svg>
      <span>www.braystone-works.net</span>
    </li>
  </ul>

  <div class="cover-name">
    <span class="mark-dot"></span>
    <span class="company">BRAYSTONE WORKWRIGHTS, INC.</span>
  </div>
  <p class="tagline">From Concept to Completion</p>

  <ul class="service-list">
    <li><svg viewBox="0 0 20 16"><path d="M2 8l6 6L18 2" fill="none" stroke="var(--tick-blue)" stroke-width="3"/></svg>Infrared imaging</li>
    <li><svg viewBox="0 0 20 16"><path d="M2 8l6 6L18 2" fill="none" stroke="var(--tick-blue)" stroke-width="3"/></svg>Data Cable Testing</li>
    <li><svg viewBox="0 0 20 16"><path d="M2 8l6 6L18 2" fill="none" stroke="var(--tick-blue)" stroke-width="3"/></svg>Fiber Optics Testing &amp; Repair, Utility Locates</li>
    <li><svg viewBox="0 0 20 16"><path d="M2 8l6 6L18 2" fill="none" stroke="var(--tick-blue)" stroke-width="3"/></svg>Preventative Maintenance</li>
    <li><svg viewBox="0 0 20 16"><path d="M2 8l6 6L18 2" fill="none" stroke="var(--tick-blue)" stroke-width="3"/></svg>Lighting Inspections Electrical Equipment Cleaning</li>
    <li><svg viewBox="0 0 20 16"><path d="M2 8l6 6L18 2" fill="none" stroke="var(--tick-blue)" stroke-width="3"/></svg>Automatic Transfer Switch Testing</li>
    <li><svg viewBox="0 0 20 16"><path d="M2 8l6 6L18 2" fill="none" stroke="var(--tick-blue)" stroke-width="3"/></svg>LED Upgrades</li>
  </ul>
</main>
</body>
</html>
```